CFO services graphic design

I own a business consulting firm called Marlowe Consulting and we need a graphic for CFO services in our colours and branding. The attached file "CFO services to be put into Marlowe consulting theme", shows the content for the design. The two other files show the theme and colours for the new design.

```html
<!DOCTYPE html>
<html lang="en">
<head>
<meta charset="utf-8">
<title>Chief Financial Officer Services</title>
<link href="https://fonts.googleapis.com/css2?family=Poppins:wght@400;500;600&display=swap" rel="stylesheet">
<style>
  :root {
    --page: #ffffff;
    --halo-outer: #f2f3f6;
    --halo-mid: #e8e9ec;
    --halo-inner: #e0e1e4;
    --ring-dark: #1a44b8;
    --ring-light: #5ec8f0;
    --ring-pale: #edf1fb;
    --core: #1552c4;
    --cost: #62c6cc;
    --capital: #21b5d4;
    --invest: #1f9bd8;
    --perform: #2584c6;
    --budget: #1f72b8;
    --risk: #0f6b78;
    --compliance: #0f82a0;
    --comms: #1569aa;
    --ink: #ffffff;
  }
  html, body { margin: 0; padding: 0; overflow: hidden; background: var(--page); }
  .canvas { width: 1168px; height: 1200px; display: block; }
  .services-wheel { width: 1168px; height: 1200px; display: block; font-family: "Poppins", sans-serif; }
  .halo-outer { fill: var(--halo-outer); }
  .halo-mid { fill: var(--halo-mid); }
  .halo-inner { fill: var(--halo-inner); }
  .node-backing { fill: #f6f7f9; }
  .core-backing { fill: var(--ring-pale); }
  .core { fill: var(--core); }
  .ring-light { fill: none; stroke: var(--ring-light); stroke-width: 3; }
  .ring-dark { fill: none; stroke: var(--ring-dark); stroke-width: 3; }
  .link-light { stroke: var(--ring-light); stroke-width: 3; }
  .link-dark { stroke: var(--ring-dark); stroke-width: 3; }
  .dot-light { fill: var(--ring-light); }
  .dot-dark { fill: var(--ring-dark); }
  .icon { fill: none; stroke: var(--ink); stroke-width: 3.5; stroke-linecap: round; stroke-linejoin: round; }
  .icon-solid { fill: var(--ink); }
  .title { fill: var(--ink); font-size: 45px; font-weight: 600; text-anchor: middle; }
  .label { fill: var(--ink); font-size: 27px; font-weight: 500; text-anchor: middle; }
  .note { fill: var(--ink); font-size: 18.5px; font-weight: 400; text-anchor: middle; }
  .fill-cost { fill: var(--cost); }
  .fill-capital { fill: var(--capital); }
  .fill-invest { fill: var(--invest); }
  .fill-perform { fill: var(--perform); }
  .fill-budget { fill: var(--budget); }
  .fill-risk { fill: var(--risk); }
  .fill-compliance { fill: var(--compliance); }
  .fill-comms { fill: var(--comms); }
</style>
</head>
<body>
<div class="canvas">
<svg class="services-wheel" viewBox="0 0 1904 1956" xmlns="http://www.w3.org/2000/svg" role="img" aria-label="Chief Financial Officer services wheel">
  <defs>
    <path id="arc-outer" d="M -163 0 A 163 163 0 0 1 163 0"/>
  </defs>

  <!-- background halos -->
  <circle class="halo-outer" cx="970" cy="980" r="585"/>
  <circle class="halo-mid" cx="970" cy="980" r="485"/>
  <circle class="halo-inner" cx="970" cy="980" r="387"/>

  <!-- connectors -->
  <line class="link-light" x1="970" y1="690" x2="970" y2="572"/>
  <line class="link-light" x1="970" y1="1270" x2="970" y2="1390"/>
  <line class="link-light" x1="1250" y1="980" x2="1380" y2="980"/>
  <line class="link-light" x1="690" y1="980" x2="561" y2="980"/>
  <line class="link-dark" x1="1170" y1="780" x2="1260" y2="691"/>
  <line class="link-dark" x1="1170" y1="1180" x2="1260" y2="1270"/>
  <line class="link-dark" x1="770" y1="780" x2="680" y2="691"/>
  <line class="link-dark" x1="770" y1="1180" x2="680" y2="1270"/>

  <!-- core -->
  <g class="core-hub">
    <circle class="core-backing" cx="970" cy="980" r="296"/>
    <circle class="ring-light" cx="970" cy="980" r="280"/>
    <path class="ring-dark" d="M 874 718 A 280 280 0 0 0 690 980" transform="rotate(0 970 980)"/>
    <circle class="ring-dark" cx="970" cy="980" r="266" stroke-dasharray="250 170"/>
    <circle class="core" cx="970" cy="980" r="262"/>
    <text class="title" x="970" y="975">CHIEF FINANCIAL</text>
    <text class="title" x="970" y="1025">OFFICER SERVICES</text>
  </g>

  <!-- top: cost accounting -->
  <g class="service-node" transform="translate(970 408)">
    <circle class="node-backing" r="180"/>
    <circle class="ring-light" r="163"/>
    <use href="#arc-outer" class="ring-dark"/>
    <circle class="fill-cost" r="145"/>
    <g class="icon" transform="translate(0 -80)">
      <path d="M -30 -40 H 20 V 28 H -28 V -32 Q -40 -40 -30 -40 Z"/>
      <path d="M -40 -34 H -28"/>
      <path d="M -18 -25 H 8 M -18 -14 H 10 M -18 -3 H 10 M -18 8 H 10 M -18 19 H 10"/>
      <path d="M -28 28 V 38 H 34 V 28 H -28"/>
      <circle cx="18" cy="-28" r="14"/>
      <path d="M 28 -18 L 44 -2"/>
    </g>
    <text class="label" x="0" y="13">COST ACCOUNTING</text>
    <text class="label" x="0" y="45">&amp; COST</text>
    <text class="label" x="0" y="77">MANAGEMENT</text>
  </g>
  <circle class="dot-light" cx="970" cy="572" r="11"/>

  <!-- top right: capital structure -->
  <g class="service-node" transform="translate(1376 576)">
    <circle class="node-backing" r="180"/>
    <circle class="ring-light" r="163"/>
    <use href="#arc-outer" class="ring-dark" transform="rotate(225)"/>
    <circle class="fill-capital" r="145"/>
    <g class="icon" transform="translate(0 -62)">
      <path d="M -12 -30 H 12 M -10 -38 H 10"/>
      <path d="M -12 -24 Q -30 -8 -28 12 Q -26 28 0 28 Q 26 28 28 12 Q 30 -8 12 -24 Z"/>
      <path d="M 7 -4 Q 0 -10 -6 -6 Q -10 0 0 3 Q 10 6 6 12 Q 0 16 -7 10 M 0 -12 V 18"/>
    </g>
    <text class="label" x="0" y="0">CAPTIAL</text>
    <text class="label" x="0" y="31">STRUCTURE &amp; THE</text>
    <text class="label" x="0" y="62">COST OF CAPITAL</text>
  </g>
  <circle class="dot-dark" cx="1260" cy="691" r="11"/>

  <!-- right: investment decisions -->
  <g class="service-node" transform="translate(1543 980)">
    <circle class="node-backing" r="180"/>
    <circle class="ring-light" r="163"/>
    <use href="#arc-outer" class="ring-dark" transform="rotate(90)"/>
    <circle class="fill-invest" r="145"/>
    <g transform="translate(0 -66)">
      <rect class="icon-solid" x="-30" y="0" width="9" height="22"/>
      <rect class="icon-solid" x="-14" y="10" width="9" height="12"/>
      <rect class="icon-solid" x="2" y="4" width="9" height="18"/>
      <rect class="icon-solid" x="18" y="-12" width="9" height="34"/>
      <path class="icon" d="M -30 -10 L -14 4 L 2 -8 L 30 -30 M 18 -30 H 30 V -18"/>
    </g>
    <text class="label" x="0" y="0">LONG-TERM &amp;</text>
    <text class="label" x="0" y="31">SHORT-TERM</text>
    <text class="label" x="0" y="62">INVESTMENT</text>
    <text class="label" x="0" y="93">DECISIONS</text>
  </g>
  <circle class="dot-light" cx="1380" cy="980" r="11"/>

  <!-- bottom right: performance -->
  <g class="service-node" transform="translate(1376 1387)">
    <circle class="node-backing" r="180"/>
    <circle class="ring-light" r="163"/>
    <use href="#arc-outer" class="ring-dark" transform="rotate(315)"/>
    <circle class="fill-perform" r="145"/>
    <g transform="translate(0 -38)">
      <path class="icon" d="M -44 0 A 44 44 0 0 1 44 0" stroke-width="6"/>
      <path class="icon-solid" d="M 10 -30 L 14 -27 L 2 -4 Q -2 2 -8 -2 Q -10 -6 -6 -10 Z"/>
    </g>
    <text class="label" x="0" y="12">PERFORMANCE</text>
    <text class="label" x="0" y="43">EVALUATION</text>
  </g>
  <circle class="dot-dark" cx="1260" cy="1270" r="11"/>

  <!-- bottom: budgeting -->
  <g class="service-node" transform="translate(970 1555)">
    <circle class="node-backing" r="180"/>
    <circle class="ring-light" r="163"/>
    <use href="#arc-outer" class="ring-dark" transform="rotate(180)"/>
    <circle class="fill-budget" r="145"/>
    <g class="icon" transform="translate(0 -72)">
      <path d="M -38 -8 A 40 40 0 0 1 -4 -44 V 0 L 30 30 A 40 40 0 0 1 -16 34"/>
      <path d="M 4 -44 A 40 40 0 0 1 40 -12 H 4 Z"/>
      <path d="M 4 -4 H 40 A 40 40 0 0 1 30 20 Z"/>
      <circle cx="-26" cy="22" r="19"/>
      <path d="M -21 15 Q -26 11 -30 15 Q -33 20 -26 22 Q -19 24 -22 29 Q -26 33 -31 29 M -26 9 V 35"/>
    </g>
    <text class="label" x="0" y="17">BUDGETING</text>
    <text class="label" x="0" y="48">&amp; STRATEGIC</text>
    <text class="label" x="0" y="79">PLANNING</text>
  </g>
  <circle class="dot-light" cx="970" cy="1390" r="11"/>

  <!-- bottom left: risk -->
  <g class="service-node" transform="translate(565 1387)">
    <circle class="node-backing" r="180"/>
    <circle class="ring-light" r="163"/>
    <use href="#arc-outer" class="ring-dark" transform="rotate(45)"/>
    <circle class="fill-risk" r="145"/>
    <g transform="translate(0 -58)">
      <path class="icon" d="M 0 -42 L 42 34 H -42 Z"/>
      <rect class="icon-solid" x="-4" y="-16" width="8" height="28"/>
      <rect class="icon-solid" x="-4" y="18" width="8" height="8"/>
    </g>
    <text class="label" x="0" y="22">RISK</text>
    <text class="label" x="0" y="53">MANAGEMENT</text>
  </g>
  <circle class="dot-dark" cx="680" cy="1270" r="11"/>

  <!-- left: compliance -->
  <g class="service-node" transform="translate(397 980)">
    <circle class="node-backing" r="180"/>
    <circle class="ring-light" r="163"/>
    <use href="#arc-outer" class="ring-dark" transform="rotate(270)"/>
    <circle class="fill-compliance" r="145"/>
    <g class="icon" transform="translate(-6 -60)">
      <path d="M 14 40 H -28 Q -34 40 -34 34 V -34 Q -34 -40 -28 -40 H 4 L 24 -20 V -6"/>
      <path d="M 4 -40 V -20 H 24"/>
      <path d="M -24 -10 H 4 M -24 6 H -2 M -24 22 H -6"/>
      <path d="M 30 0 L 48 6 V 20 Q 48 34 30 42 Q 12 34 12 20 V 6 Z"/>
      <path d="M 22 20 L 28 26 L 38 14"/>
    </g>
    <text class="label" x="0" y="23">COMPLIANCE:</text>
    <text class="note" x="-4" y="55">tax, legal &amp; regulatory</text>
  </g>
  <circle class="dot-light" cx="561" cy="980" r="11"/>

  <!-- top left: communication -->
  <g class="service-node" transform="translate(565 576)">
    <circle class="node-backing" r="180"/>
    <circle class="ring-light" r="163"/>
    <use href="#arc-outer" class="ring-dark" transform="rotate(135)"/>
    <circle class="fill-comms" r="145"/>
    <g class="icon" transform="translate(0 -70)">
      <path d="M -44 -30 Q -44 -36 -38 -36 H 14 Q 20 -36 20 -30 V 2 Q 20 8 14 8 H -22 L -36 18 V 8 H -38 Q -44 8 -44 2 Z"/>
      <path d="M -34 -22 H 6 M -34 -12 H 6 M -34 -2 H -4"/>
      <path d="M 26 -24 H 38 Q 44 -24 44 -18 V 14 Q 44 20 38 20 H 36 V 30 L 22 20 H -14 Q -20 20 -20 14"/>
    </g>
    <text class="label" x="0" y="-5">COMMUNICATION:</text>
    <text class="note" x="-4" y="24">Board of Directors,</text>
    <text class="note" x="0" y="47">creditors, owners, investors,</text>
    <text class="note" x="-4" y="69">credit rating agencies</text>
  </g>
  <circle class="dot-dark" cx="680" cy="691" r="11"/>
</svg>
</div>
</body>
</html>
```